Home Design company focused on remodel and enhancement of kitchens and bathroorms

I already have a logo designed by ArtHarbor, I now need a design for my business cards.
The company is in the remodeling and enhancement industry for homes, focusing on kitchens and bathrooms, however, we can remodel or enhance every room in a home, an office space, etc.

The company's name is VELMOR HOME DESIGN, LLC

We'll focus on clients in the Rio Grande Valley, Texas. Primarily McAllen, Edinburg, Pharr, Mission, Brownsville and South Padre Island.

The design on the business card should transmit reliability, professionalism anda bit of upscale design.

The logo is in black and white, and would like to keep it that way.

The information that needs to be printed in the business cards is:
Company's name: Velmor Home Design
Company's Logo (attached)
My name: Noel Bramwit
Address, phone and email:
2715 N Parkline Road, Ste 348
Larkmont, ST 00417
(555) 555 0187
nbramwit@velmordesign.example
Website: velmordesign.example

```html
<!DOCTYPE html>
<html lang="en">
<head>
<meta charset="utf-8">
<title>Velmor Home Design – Business Card</title>
<link rel="stylesheet" href="https://fonts.googleapis.com/css2?family=Nunito+Sans:wght@400;700;800&display=swap">
<style>
  :root {
    --stage: #9a9a9a;
    --stage-light: #bdbdbd;
    --ink: #000000;
    --paper: #ffffff;
    --band: #999999;
    --text: #111111;
  }
  html, body {
    margin: 0;
    padding: 0;
    width: 1200px;
    height: 1005px;
    overflow: hidden;
  }
  body {
    background: radial-gradient(ellipse at 50% 42%, var(--stage-light) 0%, var(--stage) 45%, #808080 100%);
    font-family: "Nunito Sans", sans-serif;
    position: relative;
  }
  .card {
    position: absolute;
    top: 175px;
    width: 469px;
    height: 656px;
    overflow: hidden;
  }
  .card--front { left: 89px; background: var(--ink); }
  .card--back { left: 643px; background: var(--paper); }

  .brand {
    position: absolute;
    display: flex;
    align-items: center;
    gap: 18px;
    color: var(--paper);
  }
  .brand__mark {
    width: 30px;
    height: 30px;
    background: var(--paper);
    flex: none;
  }
  .brand__name {
    font-weight: 400;
    letter-spacing: 0.26em;
    line-height: 1.08;
    text-transform: uppercase;
  }
  .card--front .brand { left: 92px; top: 294px; }
  .card--front .brand__name { font-size: 22px; }
  .card--back .brand { left: 98px; top: 90px; }
  .card--back .brand__name { font-size: 21px; }

  .back__top {
    position: absolute;
    left: 0; top: 0;
    width: 469px;
    height: 275px;
    background: var(--ink);
  }
  .back__roof {
    position: absolute;
    left: 0; top: 0;
  }
  .back__bottom {
    position: absolute;
    left: 0; bottom: 0;
    width: 469px;
    height: 22px;
    background: var(--ink);
  }
  .company {
    position: absolute;
    right: 10px;
    top: 303px;
    margin: 0;
    font-size: 23px;
    font-weight: 800;
    letter-spacing: 0.03em;
    color: var(--text);
  }
  .person {
    position: absolute;
    left: 0;
    top: 392px;
    width: 266px;
    height: 39px;
    background: var(--band);
    display: flex;
    align-items: center;
  }
  .person__name {
    margin: 0 0 0 26px;
    font-size: 21px;
    font-weight: 800;
    letter-spacing: 0.05em;
    color: var(--text);
  }
  .contact {
    position: absolute;
    left: 25px;
    top: 451px;
    margin: 0;
    font-size: 20px;
    color: var(--text);
    font-style: normal;
    line-height: 30px;
  }
  .contact p { margin: 0; }
  .contact__address { margin-bottom: 16px !important; }
  .contact strong { font-weight: 800; }
</style>
</head>
<body>
  <section class="card card--front" aria-label="Card front">
    <div class="brand">
      <span class="brand__mark"></span>
      <span class="brand__name">Velmor<br>Home<br>Design</span>
    </div>
  </section>

  <section class="card card--back" aria-label="Card back">
    <div class="back__top"></div>
    <svg class="back__roof" width="469" height="280" viewBox="0 0 469 280" aria-hidden="true">
      <polygon points="294,276 384.6,214 469,268 469,276" fill="#ffffff"/>
      <polygon points="323,276 384.6,233 460,276" fill="#000000"/>
    </svg>
    <div class="brand">
      <span class="brand__mark"></span>
      <span class="brand__name">Velmor<br>Home<br>Design</span>
    </div>

    <h1 class="company">VELMOR HOME DESIGN</h1>

    <div class="person">
      <h2 class="person__name">NOEL BRAMWIT</h2>
    </div>

    <address class="contact">
      <p class="contact__address">2715 N Parkline Road, Ste 348<br>Larkmont, ST 00417</p>
      <p><strong>Phone:</strong> (555) 555 0187</p>
      <p><strong>E mail:</strong> nbramwit@velmordesign.example</p>
      <p><strong>Web:</strong> velmordesign.example</p>
    </address>

    <div class="back__bottom"></div>
  </section>
</body>
</html>
```